A new customer-driven VC fund for Enterprise IT Startups

I am bringing together a global group of customers (CIOs, CTOs, CISOs of Beacon 3000 companies) to help me identify and diligence best-of-breed Enterprise IT startups so I can invest in them via my new venture capital fund, Larkfen Ventures. In many ways, this is a new model for a VC fund and my goal is to revolutionize Venture Capital so that we hit the bull's eye in investing way more often in what is otherwise a guessing game for most VCs. So in the website, I'd like to capture the essences of global reach, best-of-breed, breakthrough innovation. I also want it to convey the ability of Larkfen Ventures to create category winners (i.e., if you want to be a market leader as a startup, you must take an investment from Larkfen Ventures).
My current website is www.larkfen-ventures.example - please use the content from the website within your design but please DO NOT use the design elements from the current website. INSTEAD, I'm looking for new and creative ideas on how I can leverage the existing content in a more appealing design -- any designs that look remotely similar to the existing website will be immediately declined.
I also want to ensure that the web design is mobile friendly.
Target Market(s)
Startup founders, potential investors, and other VCs
Industry/Entity Type
Venture Capital
Coding
Coded - Design and coding required
Number of Pages Required
1 page
Look and feel
Each slider illustrates characteristics of the customer's brand and the style your logo design should communicate.

```html
<!DOCTYPE html>
<html lang="en">
<head>
<meta charset="utf-8">
<title>Larkfen Ventures</title>
<link rel="stylesheet" href="https://fonts.googleapis.com/css2?family=Montserrat:wght@500;600;700;800&family=Arimo:wght@400;700&display=swap">
<style>
:root{
  --blue:#3a8db5;
  --band:#3e8fb8;
  --ink:#2e2e2e;
  --muted:#6b6b6b;
  --black:#000;
  --white:#fff;
  --green:#8cc63f;
  --teal:#3fc08f;
  --navy:#3c5ba6;
  --cyan:#3ec6d8;
  --royal:#2f6fcb;
  --sky:#3a8fd6;
}
*{box-sizing:border-box;margin:0;padding:0}
html,body{width:1200px;height:4594px;overflow:hidden}
body{position:relative;background:var(--white);color:var(--ink);font-family:"Arimo",Arial,sans-serif}
.abs{position:absolute}
h1,h2,h3,.brand,.nav a,.btn{font-family:"Montserrat",sans-serif}
.section-title{position:absolute;left:0;width:1200px;text-align:center;font-size:35px;font-weight:700;letter-spacing:.5px;color:var(--ink)}
.section-sub{position:absolute;left:300px;width:600px;text-align:center;font-size:13.5px;line-height:25px;color:var(--muted)}
.btn{display:inline-block;border:2px solid var(--blue);color:var(--blue);border-radius:24px;font-size:13px;font-weight:600;padding:10px 20px;text-transform:uppercase;background:var(--white)}

/* header */
.site-header{position:absolute;left:0;top:0;width:1200px;height:125px;background:var(--black);border-bottom:2px solid #555}
.brand{position:absolute;color:var(--white);font-weight:700;text-transform:uppercase;letter-spacing:1px}
.site-header .brand{left:112px;top:34px;font-size:30px;line-height:31px;width:260px}
.brand-dot{display:inline-block;width:18px;height:18px;border-radius:50%;background:var(--blue);margin-right:8px;vertical-align:2px}
.nav{position:absolute;top:82px;left:484px;display:flex;gap:45px}
.nav a{color:var(--white);text-decoration:none;font-size:13.5px;font-weight:700;text-transform:uppercase}
.nav a.active{color:var(--blue)}
.social{position:absolute;display:flex;gap:7px}
.social span{width:36px;height:36px;border:2px solid var(--white);border-radius:50%;display:block}
.site-header .social{left:880px;top:23px}

/* hero */
.hero{position:absolute;left:0;top:127px;width:1200px;height:755px;overflow:hidden}
.hero-photo{position:absolute;inset:0;background:linear-gradient(180deg,#6a747c 0%,#3d464d 35%,#262d32 62%,#2c5f7b 86%,#3a8db5 100%)}
.hero h1{position:absolute;left:0;top:125px;width:1200px;text-align:center;color:var(--white);font-size:78px;font-weight:700;letter-spacing:1px}
.hero .tagline{position:absolute;left:250px;top:222px;width:700px;text-align:center;color:var(--white);font-family:"Montserrat",sans-serif;font-size:27px;font-weight:500;line-height:38px;text-transform:uppercase}
.hero .cta{position:absolute;left:511px;top:316px;width:180px;height:58px;border-radius:29px;background:var(--blue);color:var(--white);font-family:"Montserrat",sans-serif;font-weight:700;font-size:16px;line-height:58px;text-align:center}
.dots{position:absolute;left:38px;top:478px}
.dots i{display:block;width:9px;height:9px;border-radius:50%;background:var(--white);margin-bottom:9px}
.dots i.on{background:var(--blue)}

/* who we are */
.card{position:absolute;top:1070px;width:307px;height:443px;border:2px solid #e8e8e8;border-radius:16px;background:var(--white);box-shadow:0 3px 10px rgba(0,0,0,.05);text-align:center}
.card svg{margin-top:28px}
.card h3{font-size:20px;font-weight:700;line-height:31px;margin-top:8px;text-transform:uppercase}
.card p{font-size:13px;line-height:25.5px;color:var(--muted);padding:8px 30px 0}
.card .btn{position:absolute;left:88px;bottom:28px;width:130px}

/* numbers */
.numbers{position:absolute;left:0;top:1589px;width:1200px;height:480px;background:var(--band)}
.numbers .section-title{color:var(--white);top:48px}
.numbers .section-sub{color:#eaf4f9;top:102px}
.stat{position:absolute;top:168px;width:240px;text-align:center;color:var(--white)}
.stat .ring{width:120px;height:120px;border:2px solid var(--white);border-radius:50%;margin:0 auto;display:flex;align-items:center;justify-content:center}
.stat b{display:block;font-family:"Montserrat",sans-serif;font-size:32px;font-weight:700;margin-top:14px}
.stat p{font-size:13px;line-height:25px;padding:6px 30px 0}

/* focus */
.focus-label{position:absolute;font-family:"Montserrat",sans-serif;font-size:16.5px;font-weight:600;line-height:25px;color:var(--ink);text-transform:uppercase}
.petal{position:absolute;width:122px;height:122px}
.petal-icon{position:absolute;width:60px;height:60px}

/* team */
.team{position:absolute;left:0;top:2782px;width:1200px;height:625px;background:linear-gradient(180deg,#f3f4f6,#eceef1)}
.member{position:absolute;width:242px;text-align:center}
.member .photo{width:160px;height:160px;border-radius:50%;margin:0 auto;border:5px solid var(--white)}
.member h3{font-size:17.5px;font-weight:600;margin-top:15px;color:var(--ink)}
.member .role{font-size:13.5px;line-height:20px;color:var(--blue);margin-top:4px}
.member .bio{font-size:13.5px;line-height:21px;color:var(--muted);margin-top:14px;padding:0 8px}
.member.featured h3,.member.featured .role,.member.featured .bio{color:var(--white)}
.featured-bg{position:absolute;left:357px;top:3046px;width:243px;height:280px;background:var(--blue)}
.chev{position:absolute;top:3080px}

/* engine */
.engine-col{position:absolute;top:3620px;width:300px;text-align:center}
.engine-col h3{font-size:19px;font-weight:600;margin-top:20px;text-transform:uppercase}
.engine-col p{font-size:13px;line-height:26px;color:var(--muted);padding:22px 22px 0;height:156px}
.engine-col .btn{width:134px;margin-top:12px}

/* footer */
.footer-art{position:absolute;left:0;top:4020px;width:1200px;height:574px;background:linear-gradient(180deg,#ffffff 0%,#9ec8dc 14%,#3a8db5 32%,#0d2330 48%,#000 60%)}
.footer-brand{left:400px;top:4258px;width:400px;text-align:center;font-size:50px;line-height:56px}
.footer-nav{position:absolute;left:0;top:4407px;width:1200px;display:flex;justify-content:center;gap:40px}
.footer-nav a{color:var(--white);text-decoration:none;font-family:"Montserrat",sans-serif;font-size:13.5px;font-weight:600;text-transform:uppercase}
.footer .social{left:495px;top:4457px}
.copyright{position:absolute;left:0;top:4518px;width:1200px;text-align:center;color:var(--white);font-size:14px}
</style>
</head>
<body>

<header class="site-header">
  <div class="brand"><span class="brand-dot"></span>Larkfen<br>Ventures</div>
  <nav class="nav">
    <a class="active" href="#">Home</a>
    <a href="#">About</a>
    <a href="#">Network</a>
    <a href="#">Team &amp; Advisors</a>
    <a href="#">GTM Engine</a>
  </nav>
  <div class="social"><span></span><span></span><span></span><span></span><span></span></div>
</header>

<section class="hero">
  <div class="hero-photo" role="img" aria-label="Photo of a businessman climbing a long staircase between city skyscrapers, framed by a large blue zigzag arrow rising to the right"></div>
  <h1>LARKFEN VENTURES</h1>
  <p class="tagline">We invest in enterprise IT startups at the product-market-fit stage</p>
  <div class="cta">GET STARTED</div>
  <div class="dots"><i></i><i class="on"></i><i></i></div>
</section>

<h2 class="section-title" style="top:930px">WHO WE ARE</h2>
<p class="section-sub" style="top:986px">We only invest in post-product, post-revenue Enterprise IT startups. Usually, this means you're at Seed Extension to Series A stage.</p>

<article class="card" style="left:110px">
  <svg width="100" height="80" viewBox="0 0 100 80" fill="none" stroke="#3a8db5" stroke-width="3">
    <circle cx="50" cy="18" r="12"/><circle cx="20" cy="26" r="9"/><circle cx="80" cy="26" r="9"/>
    <path d="M28 75V55a22 22 0 0 1 44 0v20"/><path d="M4 72V55a16 16 0 0 1 24-12"/><path d="M96 72V55a16 16 0 0 0-24-12"/>
  </svg>
  <h3>Customers</h3>
  <p>Hundreds of the earliest-adopting CIOs, CTOs, and CISOs from Beacon 3000 to Cloud-First companies are a part of our exclusive network. An investment from Larkfen Ventures will give you immediate and exclusive access to of buyers around the world.</p>
  <span class="btn">Read More</span>
</article>
<article class="card" style="left:446px">
  <svg width="100" height="80" viewBox="0 0 100 80" fill="none" stroke="#3a8db5" stroke-width="3">
    <text x="12" y="20" fill="#3a8db5" stroke="none" font-size="20" font-family="Arial">$</text>
    <rect x="8" y="50" width="9" height="26"/><rect x="22" y="42" width="9" height="34"/><rect x="36" y="46" width="9" height="30"/><rect x="50" y="34" width="9" height="42"/><rect x="64" y="28" width="9" height="48"/><rect x="78" y="18" width="9" height="58"/>
    <path d="M10 40 30 30 45 36 62 20 84 6"/>
  </svg>
  <h3>Our Investment</h3>
  <p>We only invest in startups that have broad &amp; immediate applicability across a global CIO base and are solving critical problems. To give our portfolio companies a truly unfair competitive advantage, we do not invest in competitive startups.</p>
  <span class="btn">Read More</span>
</article>
<article class="card" style="left:781px">
  <svg width="100" height="80" viewBox="0 0 100 100" fill="none" stroke="#3a8db5" stroke-width="3">
    <path d="M20 60 62 22 80 62Z"/><path d="M20 60 28 72 42 62"/><path d="M32 68 40 86 50 82 44 64"/>
    <path d="M70 16l6-10M80 28l12-4M76 20l10-8"/>
  </svg>
  <h3>Customer<br>Led Investments</h3>
  <p>A global roster of CIOs leads our investment decision-making process. We also share candid, unfiltered feedback from dozens of customers via a Larkfen Memo™ with every single startup who presents to us</p>
  <span class="btn">Read More</span>
</article>

<section class="numbers">
  <h2 class="section-title">STRENGTH IN NUMBERS</h2>
  <p class="section-sub" style="left:200px;width:800px">We collect and analyze monthly purchase intent data from a global network of IT decision-makers.</p>
  <div class="stat" style="left:114px">
    <div class="ring"><svg width="44" height="36" viewBox="0 0 44 36" fill="#fff"><rect x="4" y="18" width="5" height="14"/><rect x="13" y="10" width="5" height="22"/><rect x="22" y="20" width="5" height="12"/><rect x="31" y="6" width="5" height="26"/><rect x="0" y="33" width="44" height="3"/><rect x="0" y="0" width="3" height="36"/></svg></div>
    <b>500+</b><p>Early adopting, influential CIOs, CTOs, CISOs and IT decision-makers</p>
  </div>
  <div class="stat" style="left:360px">
    <div class="ring"><svg width="44" height="40" viewBox="0 0 44 40" fill="none" stroke="#fff" stroke-width="5"><circle cx="16" cy="22" r="8" stroke-dasharray="4 2.3"/><circle cx="33" cy="10" r="5" stroke-width="4" stroke-dasharray="3 1.6"/><circle cx="34" cy="31" r="4" stroke-width="3.5" stroke-dasharray="2.5 1.4"/></svg></div>
    <b>$100B+</b><p>Annual enterprise technology purchasing budget across our network</p>
  </div>
  <div class="stat" style="left:606px">
    <div class="ring"><svg width="44" height="34" viewBox="0 0 44 34" fill="#fff"><circle cx="22" cy="9" r="7"/><circle cx="8" cy="12" r="5"/><circle cx="36" cy="12" r="5"/><path d="M10 34a12 12 0 0 1 24 0Z"/><path d="M0 30a8 8 0 0 1 13-7l-3 7Z"/><path d="M44 30a8 8 0 0 0-13-7l3 7Z"/></svg></div>
    <b>15</b><p>Countries represented in our current network</p>
  </div>
  <div class="stat" style="left:852px">
    <div class="ring"><svg width="36" height="36" viewBox="0 0 36 36" fill="#fff"><rect x="2" y="6" width="32" height="28" rx="2"/><rect x="8" y="0" width="4" height="9"/><rect x="24" y="0" width="4" height="9"/><g fill="#3e8fb8"><rect x="6" y="14" width="5" height="4"/><rect x="13" y="14" width="5" height="4"/><rect x="20" y="14" width="5" height="4"/><rect x="27" y="14" width="4" height="4"/><rect x="6" y="21" width="5" height="4"/><rect x="13" y="21" width="5" height="4"/><rect x="20" y="21" width="5" height="4"/><rect x="27" y="21" width="4" height="4"/><rect x="6" y="28" width="5" height="3"/><rect x="13" y="28" width="5" height="3"/></g></svg></div>
    <b>500+</b><p>Purchase intent data points collected monthly</p>
  </div>
</section>

<h2 class="section-title" style="top:2122px">INVESTMENT FOCUS AREAS</h2>
<p class="section-sub" style="top:2180px">We only invest in post-product, post-revenue Enterprise IT startups. Usually, this means you're at Seed Extension to Series A stage.</p>

<svg class="abs" style="left:0;top:2270px" width="1200" height="450" viewBox="0 2270 1200 450">
  <g stroke-width="2" fill="none">
    <line x1="375" y1="2328" x2="460" y2="2328" stroke="#8cc63f"/>
    <line x1="740" y1="2333" x2="830" y2="2333" stroke="#3fc08f"/>
    <line x1="298" y1="2500" x2="362" y2="2500" stroke="#3c5ba6"/>
    <line x1="838" y1="2494" x2="893" y2="2494" stroke="#3ec6d8"/>
    <line x1="385" y1="2658" x2="460" y2="2658" stroke="#2f6fcb"/>
    <line x1="740" y1="2656" x2="823" y2="2656" stroke="#3a8fd6"/>
  </g>
  <circle cx="375" cy="2328" r="5" fill="#8cc63f"/>
  <circle cx="830" cy="2333" r="5" fill="#3fc08f"/>
  <circle cx="298" cy="2500" r="5" fill="#3c5ba6"/>
  <circle cx="893" cy="2494" r="5" fill="#3ec6d8"/>
  <circle cx="385" cy="2658" r="5" fill="#2f6fcb"/>
  <circle cx="823" cy="2656" r="5" fill="#3a8fd6"/>
</svg>

<div class="petal" style="left:460px;top:2288px;background:var(--green);border-radius:50% 50% 8% 50%"></div>
<div class="petal" style="left:617px;top:2288px;background:var(--teal);border-radius:50% 50% 50% 8%"></div>
<div class="petal" style="left:362px;top:2436px;background:var(--navy);border-radius:50% 50% 8% 50%;transform:rotate(-45deg)"></div>
<div class="petal" style="left:715px;top:2436px;background:var(--cyan);border-radius:50% 50% 8% 50%;transform:rotate(135deg)"></div>
<div class="petal" style="left:460px;top:2586px;background:var(--royal);border-radius:50% 8% 50% 50%"></div>
<div class="petal" style="left:617px;top:2586px;background:var(--sky);border-radius:8% 50% 50% 50%"></div>

<svg class="petal-icon" style="left:491px;top:2319px" viewBox="0 0 60 60" fill="none" stroke="#fff" stroke-width="2.5"><path d="M30 4 52 12v18c0 14-10 22-22 26C18 52 8 44 8 30V12Z"/><rect x="21" y="28" width="18" height="14" rx="2"/><path d="M24 28v-5a6 6 0 0 1 12 0v5"/></svg>
<svg class="petal-icon" style="left:648px;top:2319px" viewBox="0 0 60 60" fill="none" stroke="#fff" stroke-width="2.5"><path d="M16 40a10 10 0 0 1 0-20 14 14 0 0 1 27-3 11 11 0 0 1 1 23Z"/><path d="M22 40v10M30 40v14M38 40v10"/><circle cx="22" cy="52" r="2"/><circle cx="38" cy="52" r="2"/></svg>
<svg class="petal-icon" style="left:393px;top:2467px" viewBox="0 0 60 60" fill="none" stroke="#fff" stroke-width="2.5"><circle cx="30" cy="26" r="18"/><path d="M30 8v36M18 18h8M34 30h8M20 34h6"/><path d="M24 44v10M36 44v10"/><circle cx="24" cy="55" r="2"/><circle cx="36" cy="55" r="2"/></svg>
<svg class="petal-icon" style="left:746px;top:2467px" viewBox="0 0 60 60" fill="none" stroke="#fff" stroke-width="2.5"><path d="M14 34a10 10 0 0 1 1-20 14 14 0 0 1 27-2 11 11 0 0 1 2 22Z"/><path d="M22 40v8M30 38v12M38 40v8"/><circle cx="22" cy="51" r="2"/><circle cx="30" cy="53" r="2"/><circle cx="38" cy="51" r="2"/></svg>
<svg class="petal-icon" style="left:491px;top:2617px" viewBox="0 0 60 60" fill="none" stroke="#fff" stroke-width="2.5"><rect x="6" y="8" width="48" height="36"/><path d="M14 16h16v12H14zM36 16h10v22H36zM14 34h16"/><path d="M22 44v8h16"/></svg>
<svg class="petal-icon" style="left:648px;top:2617px" viewBox="0 0 60 60" fill="none" stroke="#fff" stroke-width="2.5"><path d="M14 46a12 12 0 0 1 0-24 16 16 0 0 1 31-2 12 12 0 0 1 1 26Z"/><rect x="18" y="28" width="24" height="12" rx="3"/></svg>

<div class="brand" style="left:500px;top:2476px;width:210px;text-align:center;color:#555;font-size:22px;line-height:24px">Larkfen<br>Ventures</div>

<div class="focus-label" style="left:260px;top:2316px">Security</div>
<div class="focus-label" style="left:854px;top:2308px">Cloud &amp;<br>Infrastructure</div>
<div class="focus-label" style="left:213px;top:2488px">AI &amp; ML</div>
<div class="focus-label" style="left:908px;top:2481px">DevOps</div>
<div class="focus-label" style="left:198px;top:2630px;text-align:right">Networking and<br>Architecture</div>
<div class="focus-label" style="left:843px;top:2644px">SaaS</div>

<section class="team">
  <h2 class="section-title" style="top:56px">TEAM, INVESTORS &amp; ADVISORS</h2>
  <p class="section-sub" style="left:270px;width:660px;top:102px">We have built a world-class roster of executive advisors and mentors with exceptional go-to-market pedigrees to help our portfolio companies in their go-to-market journeys.</p>
</section>
<div class="featured-bg"></div>
<div class="member" style="left:108px;top:2981px">
  <div class="photo" role="img" aria-label="Portrait of Martin Hale" style="background:linear-gradient(160deg,#6a8a6e,#2f3b35)"></div>
  <h3>MARTIN HALE</h3><p class="role">Founder &amp; Ex CEO,<br>Corvane</p>
  <p class="bio">We have built a world-class roster of executive advisors and mentors with exceptional</p>
</div>
<div class="member featured" style="left:357px;top:2981px">
  <div class="photo" role="img" aria-label="Portrait of Tobias Renn" style="background:linear-gradient(160deg,#b08a7a,#4a3d38)"></div>
  <h3>TOBIAS RENN</h3><p class="role">Co-founder, Quillbase<br>($2B+ valuation)</p>
  <p class="bio" style="margin-top:8px">We have built a world-class roster of executive advisors and mentors with exceptional</p>
</div>
<div class="member" style="left:602px;top:2981px">
  <div class="photo" role="img" aria-label="Portrait of Thomas Kerrow" style="background:linear-gradient(160deg,#c9a58a,#3a2e2a)"></div>
  <h3>THOMAS KERROW</h3><p class="role">President, Ardentis</p>
  <p class="bio" style="margin-top:34px">We have built a world-class roster of executive advisors and mentors with exceptional</p>
</div>
<div class="member" style="left:849px;top:2981px">
  <div class="photo" role="img" aria-label="Portrait of Jonah Birch" style="background:linear-gradient(160deg,#d8d8d8,#8a6f60)"></div>
  <h3>JONAH BIRCH</h3><p class="role">Executive Director,<br>Fieldform</p>
  <p class="bio">We have built a world-class roster of executive advisors and mentors with exceptional</p>
</div>
<svg class="chev" style="left:70px" width="22" height="84" viewBox="0 0 22 84"><polyline points="20,2 2,42 20,82" fill="none" stroke="#888" stroke-width="2"/></svg>
<svg class="chev" style="left:1126px" width="22" height="84" viewBox="0 0 22 84"><polyline points="2,2 20,42 2,82" fill="none" stroke="#888" stroke-width="2"/></svg>

<h2 class="section-title" style="top:3464px">A GLOBAL GTM ENGINE</h2>
<p class="section-sub" style="left:250px;width:700px;top:3520px">We don't just make "customer intros", we partner with you each step of the way to help you navigate the complex landscape of enterprise sales, from key strategic accounts to strategic channel partners</p>

<div class="engine-col" style="left:119px">
  <svg width="96" height="90" viewBox="0 0 96 90" fill="none" stroke="#3a8db5" stroke-width="2.5"><rect x="40" y="4" width="52" height="40"/><path d="M50 36V26M60 36V18M70 36V22M80 36V12"/><circle cx="22" cy="14" r="8"/><circle cx="16" cy="58" r="7"/><circle cx="40" cy="58" r="7"/><circle cx="64" cy="58" r="7"/><path d="M4 86a12 12 0 0 1 24 0M28 86a12 12 0 0 1 24 0M52 86a12 12 0 0 1 24 0M22 26v16"/></svg>
  <h3>GTM Coaches</h3>
  <p>We will partner with you to navigate the complex enterprise sales process leveraging our executive network to provide product feedback, sales&nbsp; strategy</p>
  <span class="btn">Read More</span>
</div>
<div class="engine-col" style="left:449px">
  <svg width="96" height="90" viewBox="0 0 96 90" fill="none" stroke="#3a8db5" stroke-width="2.5"><circle cx="48" cy="10" r="7"/><path d="M36 32a12 12 0 0 1 24 0Z"/><circle cx="22" cy="58" r="7"/><path d="M10 82a12 12 0 0 1 24 0Z"/><circle cx="74" cy="58" r="7"/><path d="M62 82a12 12 0 0 1 24 0Z"/><path d="M40 38 28 48M56 38l12 10M36 70h24"/></svg>
  <h3>Strategic Partners</h3>
  <p>Strategic partnerships can propel a startup to the next level. Leverage our extensive network of IT Executives, Channel Partners, OEMs to accelerate your path</p>
  <span class="btn">Read More</span>
</div>
<div class="engine-col" style="left:779px">
  <svg width="96" height="90" viewBox="0 0 96 90" fill="none" stroke="#3a8db5" stroke-width="2.5"><circle cx="48" cy="46" r="20"/><ellipse cx="48" cy="46" rx="9" ry="20"/><path d="M28 46h40"/><circle cx="48" cy="6" r="4"/><circle cx="48" cy="86" r="4"/><circle cx="8" cy="46" r="4"/><circle cx="88" cy="46" r="4"/><circle cx="20" cy="18" r="4"/><circle cx="76" cy="18" r="4"/><circle cx="20" cy="74" r="4"/><circle cx="76" cy="74" r="4"/></svg>
  <h3>Global Ambassadors</h3>
  <p>A global roster of CIOs leads our investment decision-making process. We also share candid, unfiltered feedback from dozens of customers via a Larkfen Memo</p>
  <span class="btn">Read More</span>
</div>

<footer class="footer">
  <div class="footer-art" role="img" aria-label="Decorative blue zigzag arrow band running across the top of the black footer"></div>
  <div class="brand footer-brand"><span class="brand-dot" style="width:26px;height:26px"></span>Larkfen<br>Ventures</div>
  <nav class="footer-nav">
    <a href="#">Home</a><a href="#">About</a><a href="#">Network</a><a href="#">Team &amp; Advisors</a><a href="#">GTM Engine</a>
  </nav>
  <div class="social"><span></span><span></span><span></span><span></span><span></span></div>
  <p class="copyright">© Copyright 2022 Larkfen Ventures.All Rights Reserved.</p>
</footer>

</body>
</html>
```